Waterproofing specialist needs a flyer design

Our company does repair works for any leakage problems, for example, concrete roofs, balcony, toilets & bathroom, etc. We want our flyers to have a certain focus on the home services that we provide, mainly toilets & bathrooms but not leaving out the rest.

For toilet leakages, we use flood infusion method to water proof and repair toilets. Hence, we like to promote there will be No dust, No noise, No smell, No drilling, No hacking and No removal of existing tile finish. The types of chemical used to manage leakage problems are non-toxic and stops re-bar corrosion. Best of all, it only requires only One-day work. We also provide a call for free consultation.

As we do not have a good picture on waterproofing for illustration, you're welcome to come up with your own pictures that deem fit. The design should communicate reliability and safety.
---------------------------------------------------------

Hi, I have uploaded some of our project pictures for your reference. It is to show an example of what we do in waterproofing. We seal up cracked ceilings or walls basically to prevent water leakage. Understood that the pictures came from RUNFrame, as such, I have also done some research. Searching for "Water damage ceiling" is more relevant our profession. However, I did find more pictures from lenvaultery. I have uploaded one example that can be used. Do feedback to me if the uploads helped or more photos are needed to support your design.

Households

Concrete

• Pictures

```html
<!DOCTYPE html>
<html lang="en">
<head>
<meta charset="utf-8">
<title>Tidewell Waterproofing Flyer</title>
<link rel="stylesheet" href="https://fonts.googleapis.com/css2?family=Open+Sans:ital,wght@0,300;0,400;0,600;0,700;1,700&display=swap">
<style>
  :root {
    --bg: #ececec;
    --paper: #ffffff;
    --blue: #2f86cf;
    --blue-deep: #1f6fb8;
    --blue-light: #4aa3e0;
    --ink: #3a3a3a;
    --band-dark: #3d3f42;
    --water-1: #9fb0bf;
    --water-2: #6f8496;
    --badge: #7fa6c9;
  }
  * { box-sizing: border-box; margin: 0; padding: 0; }
  html, body { width: 1200px; height: 789px; overflow: hidden; }
  body {
    background: var(--bg);
    font-family: "Open Sans", Arial, sans-serif;
    color: var(--ink);
    position: relative;
  }
  .flyer {
    position: absolute;
    left: 338px; top: 24px;
    width: 524px; height: 740px;
    background: var(--paper);
    box-shadow: 0 4px 18px rgba(0,0,0,.18);
    overflow: hidden;
  }
  .water-backdrop {
    position: absolute; left: 0; top: 0; width: 100%; height: 330px;
    background: radial-gradient(ellipse at 40% 30%, var(--water-1), var(--water-2));
  }
  .brand-box {
    position: absolute; top: 26px; right: 22px;
    width: 204px; height: 78px;
    background: var(--paper); border-radius: 8px;
    display: flex; align-items: center; justify-content: center; gap: 10px;
    box-shadow: 0 2px 6px rgba(0,0,0,.2);
  }
  .brand-dot { width: 22px; height: 22px; border-radius: 50%; background: var(--blue-deep); }
  .brand-name {
    font-weight: 700; font-size: 17px; color: var(--blue-deep);
    line-height: 1.1; text-transform: uppercase; letter-spacing: .5px;
  }
  .stage { position: absolute; width: 140px; text-align: center; z-index: 2; }
  .stage-photo {
    width: 118px; height: 118px; border-radius: 50%;
    border: 4px solid var(--blue);
    background: linear-gradient(160deg, #e9ecee 0%, #c9ccc8 55%, #9c9281 100%);
    position: relative; margin: 0 auto;
  }
  .stage-label {
    position: absolute; bottom: 6px; left: 0; right: 0;
    font-size: 10px; font-weight: 700; color: #555; text-transform: uppercase;
  }
  .stage-caption {
    margin-top: -6px; position: relative;
    background: var(--paper); color: var(--blue);
    border-radius: 7px; padding: 3px 6px;
    font-size: 9px; line-height: 1.25;
    box-shadow: 0 1px 3px rgba(0,0,0,.2);
  }
  .stage.before { left: 20px; top: 92px; }
  .stage.method { left: 192px; top: 124px; }
  .stage.after { right: 16px; top: 144px; }

  .headline-band {
    position: absolute; left: 0; top: 300px; width: 100%; height: 52px;
    background: var(--blue);
    color: #fff; font-weight: 300; font-size: 34px;
    text-align: center; line-height: 52px; letter-spacing: .5px;
  }
  .services {
    position: absolute; top: 362px; width: 100%; text-align: center;
  }
  .services-lead { font-size: 19px; font-weight: 600; color: var(--ink); }
  .services-list { font-size: 21px; color: var(--blue-light); margin-top: 2px; }
  .promise-band {
    position: absolute; left: 0; top: 428px; width: 100%; height: 50px;
    background: var(--band-dark); color: #fff;
    font-size: 13px; text-align: center; text-transform: uppercase;
    display: flex; align-items: center; justify-content: center;
    padding: 0 30px; line-height: 1.3;
  }
  .safety-note {
    position: absolute; top: 490px; left: 40px; right: 40px;
    text-align: center; font-size: 14px; line-height: 1.35;
  }
  .one-day {
    position: absolute; top: 540px; left: 28px;
    font-size: 13px; font-weight: 700; font-style: italic; color: var(--blue);
  }
  .call {
    position: absolute; top: 560px; left: 28px;
    display: grid; grid-template-columns: 36px auto; column-gap: 10px; align-items: center;
  }
  .call-icon { grid-row: 1 / span 2; }
  .call-label { font-size: 19px; color: var(--ink); }
  .call-number { font-size: 28px; color: var(--blue); letter-spacing: .5px; }
  .warranty { position: absolute; right: 30px; top: 560px; }
  .footer-band {
    position: absolute; left: 0; bottom: 0; width: 100%; height: 60px;
    background: linear-gradient(90deg, var(--blue-deep), var(--blue));
    color: #fff; font-size: 14px;
    display: flex; justify-content: space-between; align-items: center;
    padding: 0 26px;
  }
</style>
</head>
<body>
  <article class="flyer">
    <div class="water-backdrop" role="img" aria-label="Water droplets on a grey surface"></div>

    <div class="brand-box">
      <span class="brand-dot"></span>
      <span class="brand-name">Tidewell<br>Waterproofing</span>
    </div>

    <figure class="stage before">
      <div class="stage-photo" role="img" aria-label="Toilet on a cracked floor before repair"><span class="stage-label">Before</span></div>
      <figcaption class="stage-caption">Cracked floor with water penetrating through the level below</figcaption>
    </figure>

    <figure class="stage method">
      <div class="stage-photo" role="img" aria-label="Toilet floor being flooded with repair solution"></div>
      <figcaption class="stage-caption">Flood infusion method used for repair</figcaption>
    </figure>

    <figure class="stage after">
      <div class="stage-photo" role="img" aria-label="Restored toilet floor after repair"><span class="stage-label">After</span></div>
      <figcaption class="stage-caption">Restoring floor to original state with cracks sealed</figcaption>
    </figure>

    <h1 class="headline-band">SPOTTED A LEAK?</h1>

    <section class="services">
      <p class="services-lead">Repair works for any leakage problems:</p>
      <p class="services-list">roofs, balcony, toilets &amp; bathroom...</p>
    </section>

    <p class="promise-band">No dust, no noise, no smell, no drilling, no hacking and<br>no removal of existing tile finish.</p>

    <p class="safety-note">Types of chemical used to manage leakage problems are non-toxic and stops re-bar corrosion.</p>

    <p class="one-day">Best of all, it only requires ONE-DAY work!</p>

    <div class="call">
      <svg class="call-icon" width="36" height="36" viewBox="0 0 36 36" aria-hidden="true">
        <circle cx="18" cy="18" r="16" fill="none" stroke="#2f86cf" stroke-width="2.5"/>
        <path d="M12 10c1-1 2.5-1 3 0l1.8 3c.4.8.2 1.6-.5 2.1l-1.2.9c.8 2.2 2.6 4 4.8 4.8l.9-1.2c.5-.7 1.3-.9 2.1-.5l3 1.8c1 .5 1 2 0 3l-1.3 1.3c-1.2 1.2-3 1.5-4.6.8-4.2-1.9-7.6-5.3-9.5-9.5-.7-1.6-.4-3.4.8-4.6z" fill="#2f86cf"/>
      </svg>
      <span class="call-label">CALL FOR FREE CONSULTATION</span>
      <span class="call-number">03 8172 4450</span>
    </div>

    <svg class="warranty" width="110" height="100" viewBox="0 0 110 100" aria-label="Warranty provided">
      <polygon points="35,4 75,4 102,30 102,70 75,96 35,96 8,70 8,30" fill="none" stroke="#7fa6c9" stroke-width="3"/>
      <rect x="0" y="36" width="110" height="24" fill="#7fa6c9"/>
      <text x="55" y="53" text-anchor="middle" font-family="Open Sans, sans-serif" font-weight="700" font-size="13" fill="#fff">WARRANTY</text>
      <text x="55" y="76" text-anchor="middle" font-family="Open Sans, sans-serif" font-weight="700" font-size="10" fill="#7fa6c9">PROVIDED</text>
    </svg>

    <footer class="footer-band">
      <span class="footer-email">tidewell@mail.com</span>
      <span class="footer-address">Harbour Lane 18, 40210 Westford</span>
    </footer>
  </article>
</body>
</html>
```